Bref créative
Edgy modern Letterhead an B. card for jet charter company
Veltaro Corporation
Professional
Peter Haldane
Founder, Chief Pilot
246 W. Harbor Ave., Suite 2020
Long Beach, CA 90815
855.5.VELTARO
phal@veltaro-example.com
veltaro-example.com
Use: Veltaro Corporation for company name

```html
<!DOCTYPE html>
<html lang="en">
<head>
<meta charset="utf-8">
<title>Veltaro Corporation – Business Card</title>
<link rel="stylesheet" href="https://fonts.googleapis.com/css2?family=Open+Sans:wght@400;700&display=swap">
<style>
  :root {
    --stage: #e9e6e1;
    --card-black: #050505;
    --card-grey: #a7a7a9;
    --ink-dark: #1c1c1c;
    --ink-light: #ffffff;
    --ink-muted: #9a9a9a;
    --shadow: rgba(0, 0, 0, 0.28);
  }
  * { box-sizing: border-box; margin: 0; padding: 0; }
  html, body {
    width: 1200px;
    height: 607px;
    overflow: hidden;
    background: var(--stage);
    font-family: "Open Sans", Arial, sans-serif;
  }
  .canvas {
    position: relative;
    width: 1200px;
    height: 607px;
  }
  .card {
    position: absolute;
    top: 178px;
    width: 511px;
    height: 280px;
    box-shadow: 0 6px 16px var(--shadow);
    overflow: hidden;
  }
  .card--front { left: 53px; background: var(--card-black); }
  .card--back  { left: 631px; background: var(--card-black); }

  .front__brand-panel {
    position: absolute;
    left: 0; top: 0;
    width: 240px; height: 100%;
    background: var(--card-grey);
  }
  .front__tab {
    position: absolute;
    left: 398px; top: 43px;
    width: 43px; height: 19px;
    background: var(--card-grey);
  }
  .wordmark {
    position: absolute;
    font-weight: 400;
    letter-spacing: 1px;
    line-height: 1;
  }
  .wordmark--front {
    left: 0; width: 240px;
    top: 98px;
    text-align: center;
    font-size: 44px;
    color: var(--ink-dark);
  }
  .wordmark--back {
    left: 0; width: 100%;
    top: 105px;
    text-align: center;
    font-size: 50px;
    color: var(--ink-light);
  }

  .contact {
    position: absolute;
    left: 276px; top: 44px;
    color: var(--ink-light);
    font-size: 11.5px;
    line-height: 16px;
  }
  .contact__name { font-weight: 700; }
  .contact__title { margin-bottom: 24px; }
  .contact__address { margin-bottom: 0; }

  .back__url {
    position: absolute;
    left: 0; width: 100%;
    bottom: 26px;
    text-align: center;
    font-size: 11px;
    color: var(--ink-muted);
  }
</style>
</head>
<body>
  <main class="canvas">
    <section class="card card--front" aria-label="Business card front">
      <div class="front__brand-panel"></div>
      <div class="front__tab"></div>
      <div class="wordmark wordmark--front">veltaro</div>
      <div class="contact">
        <p class="contact__name">Peter Haldane</p>
        <p class="contact__title">Founder, Chief Pilot</p>
        <p class="contact__address">246 W. Harbor Ave., Suite 2020</p>
        <p class="contact__address">Long Beach, CA 90815</p>
        <p>Toll Free: 855.5.VELTARO</p>
        <p>Tel: 562.555.0130</p>
        <p>Cell: 949.555.0177</p>
        <p>Fax: 562.555.0131</p>
        <p>Email: phal@veltaro-example.com</p>
      </div>
    </section>

    <section class="card card--back" aria-label="Business card back">
      <div class="wordmark wordmark--back">veltaro</div>
      <p class="back__url">www.veltaro-example.com</p>
    </section>
  </main>
</body>
</html>
```